IT Business Card --- Quorvatek
Business card information technology
Professional
Mira Dunst
Senior System Consultant
47 Fernbrook Cres
Richmond Hill, L3K2P9
Ontario, Canada.
mira.dunst@quorvatekhub.com
www.quorvatekhub.com
PNXA #4183 Voice, R&S
This is my logo in AI format

```html
<!DOCTYPE html>
<html lang="en">
<head>
<meta charset="utf-8">
<title>Quorvatek Stationery</title>
<link href="https://fonts.googleapis.com/css2?family=Open+Sans:wght@400;600;700&display=swap" rel="stylesheet">
<style>
  :root {
    --stage: #2a2a2a;
    --paper: #ffffff;
    --ink: #333333;
    --muted: #777777;
    --red: #d0121b;
    --red-deep: #8a0a10;
    --charcoal: #1d1d1d;
    --faint: #f4dcdc;
  }
  * { box-sizing: border-box; margin: 0; padding: 0; }
  html, body { width: 1200px; height: 754px; overflow: hidden; }
  body {
    background: var(--stage);
    font-family: "Open Sans", Arial, sans-serif;
    position: relative;
    color: var(--ink);
  }
  .sheet { position: absolute; overflow: hidden; }
  .sheet > svg.wave { position: absolute; left: 0; bottom: 0; width: 100%; }

  .brand { display: flex; align-items: center; gap: 6px; }
  .brand-dot { width: 14px; height: 14px; border-radius: 50%; background: var(--red); }
  .brand-name { font-weight: 700; font-size: 15px; color: var(--red); letter-spacing: .2px; line-height: 1; }

  .faint-disc { position: absolute; border-radius: 50%; background: var(--faint); opacity: .55; }

  /* Compliment slip */
  .compliment { left: 40px; top: 290px; width: 300px; height: 180px; background: var(--paper); }
  .compliment .brand { position: absolute; top: 18px; left: 18px; }
  .compliment .faint-disc { width: 120px; height: 120px; left: 150px; top: 40px; }

  /* Letterhead */
  .letterhead { left: 370px; top: 40px; width: 330px; height: 466px; background: var(--paper); }
  .letterhead .brand { position: absolute; top: 24px; left: 50%; transform: translateX(-50%); }
  .letterhead .faint-disc { width: 190px; height: 190px; left: 70px; top: 220px; }
  .letterhead .footer {
    position: absolute; right: 16px; bottom: 14px; text-align: right;
    font-size: 8px; line-height: 1.5; color: #fff;
  }

  /* Envelope */
  .envelope { left: 730px; top: 40px; width: 430px; height: 200px; background: var(--paper); }
  .envelope .flap { position: absolute; inset: 0; }
  .envelope .brand { position: absolute; top: 18px; left: 20px; }
  .envelope .return {
    position: absolute; top: 40px; left: 40px; font-size: 8px; line-height: 1.5; color: var(--muted);
  }

  /* Business cards */
  .card { width: 340px; height: 200px; top: 530px; background: var(--charcoal); border-radius: 6px; }
  .card svg { position: absolute; inset: 0; }
  .card-back { left: 370px; }
  .card-back .brand { position: absolute; left: 50%; top: 50%; transform: translate(-50%, -50%); }
  .card-back .brand-dot { width: 26px; height: 26px; }
  .card-back .brand-name { font-size: 28px; }

  .card-front { left: 730px; }
  .card-front .brand { position: absolute; top: 66px; right: 20px; }
  .card-front .person { position: absolute; left: 20px; top: 100px; }
  .person-name { font-size: 15px; font-weight: 700; color: #fff; }
  .person-role { font-size: 9px; font-weight: 600; color: var(--red); margin-top: 2px; }
  .person-cert { font-size: 8px; color: #bbbbbb; margin-top: 1px; }
  .card-front .contact {
    position: absolute; right: 20px; bottom: 14px; text-align: right;
    font-size: 8px; line-height: 1.55; color: #dddddd;
  }
</style>
</head>
<body>

<section class="sheet compliment" aria-label="Compliment slip">
  <div class="brand"><span class="brand-dot"></span><span class="brand-name">Quorvatek</span></div>
  <div class="faint-disc"></div>
  <svg class="wave" viewBox="0 0 300 60" height="60" preserveAspectRatio="none">
    <path d="M0 30 C90 10 190 14 300 0 L300 60 L0 60 Z" fill="var(--red-deep)"/>
    <path d="M0 40 C100 22 200 22 300 10 L300 60 L0 60 Z" fill="var(--red)"/>
  </svg>
</section>

<section class="sheet letterhead" aria-label="Letterhead">
  <div class="brand"><span class="brand-dot"></span><span class="brand-name">Quorvatek</span></div>
  <div class="faint-disc"></div>
  <svg class="wave" viewBox="0 0 330 110" height="110" preserveAspectRatio="none">
    <path d="M0 64 C100 18 200 18 330 0 L330 110 L0 110 Z" fill="var(--red-deep)"/>
    <path d="M0 78 C110 36 210 32 330 16 L330 110 L0 110 Z" fill="var(--red)"/>
  </svg>
  <div class="footer">
    47 Fernbrook Cres, Richmond Hill, L3K2P9, Ontario, Canada.<br>
    Tel: 905.555.0148 &nbsp; Fax: 905.555.0149<br>
    www.quorvatekhub.com
  </div>
</section>

<section class="sheet envelope" aria-label="Envelope">
  <svg class="flap" viewBox="0 0 430 200" preserveAspectRatio="none">
    <path d="M0 0 L215 110 L430 0" fill="none" stroke="#e6e6e6" stroke-width="1.5"/>
  </svg>
  <div class="brand"><span class="brand-dot"></span><span class="brand-name">Quorvatek</span></div>
  <div class="return">47 Fernbrook Cres<br>Richmond Hill, L3K2P9<br>Ontario, Canada.</div>
</section>

<section class="sheet card card-back" aria-label="Business card back">
  <svg viewBox="0 0 340 200" preserveAspectRatio="none">
    <path d="M0 150 C90 110 200 190 340 120 L340 200 L0 200 Z" fill="var(--red-deep)"/>
    <path d="M0 170 C100 130 210 200 340 145 L340 200 L0 200 Z" fill="var(--red)"/>
    <path d="M0 0 L340 0 L340 30 C230 55 120 20 0 40 Z" fill="var(--red)"/>
  </svg>
  <div class="brand"><span class="brand-dot"></span><span class="brand-name">Quorvatek</span></div>
</section>

<section class="sheet card card-front" aria-label="Business card front">
  <svg viewBox="0 0 340 200" preserveAspectRatio="none">
    <path d="M340 0 L340 52 C270 24 190 50 130 26 C100 14 80 5 66 0 Z" fill="var(--red-deep)"/>
    <path d="M340 0 L340 38 C270 10 200 38 150 16 C128 7 116 2 108 0 Z" fill="var(--red)"/>
  </svg>
  <div class="brand"><span class="brand-dot"></span><span class="brand-name">Quorvatek</span></div>
  <div class="person">
    <div class="person-name">Mira Dunst</div>
    <div class="person-role">Senior System Consultant</div>
    <div class="person-cert">PNXA #4183 Voice, R&amp;S</div>
  </div>
  <div class="contact">
    47 Fernbrook Cres<br>
    Richmond Hill, L3K2P9<br>
    Ontario, Canada.<br>
    mira.dunst@quorvatekhub.com<br>
    www.quorvatekhub.com
  </div>
</section>

</body>
</html>
```